Tessaro Lane Website

We are starting a marketing company and to do that we need a website! We want a website that will inspire and persuade to bring out the awesomeness in our clients.
What we want to see:
- Inspirational and persuasive imagery that relate to Branding.
- No cliche images eg. business man, suits and hand shakes
- We want to transform and educate our clients.
- We want to show them the path and would like our website to really act as a guide that guides them step by step through our process.
- We want the portray that we are an investment but not have a pretentious way to it. We put our heart into every project and that is how we treat our clients.
-When you submit your design please include what platform you have created for. Preference would be Wordpress or Joobla.

We have included the psd file for the wire frame, logo files, font files, site map and a link to a video we create to give you more information on what we would like to see. http://clipvault-demo.example/t/qx903LmaP

Feel free to make small modification to the logos if you think it will improve it. Your creativity and advice is most welcome.

One thing we forgot. We would like to have our contact information near the top of the website as well as at the bottom.  Here is out contact info:

Email: info@tessarolane.ca
Phone: 555-013-4829

Reason: As we are new with the platform and that we want to optimize our results, we decided to extend the deadline by 15 days. Thanks!

Target Market(s)

28-60, Male and Female, Oil field, Local Businesses, Dentists, Chiropractors, Hair salon, Construction/Renovation, Events etc

Industry/Entity Type

Investment

Requirements
Must have
• - 4 Inspirational and persuasive Imagery for the top portion of the website
- Must have a feel as if your not on a website an example of this is linked below.
http://www.pitchgallery-demo.example/design/482907/web-design-by-dalia-fenwick
Nice to have
• - Creative advice from you.
- Creative buttons for Get Free Quote and Subscribe buttons. Something out of the box that draws peoples attention. eg. a 'B' button. Just and example but still something related to branding.
Should not have
• No Cliches

```html
<!DOCTYPE html>
<html lang="en">
<head>
<meta charset="utf-8">
<title>Tessaro Lane</title>
<link href="https://fonts.googleapis.com/css2?family=PT+Sans:ital,wght@0,400;0,700;1,400&family=PT+Sans+Narrow:wght@400;700&family=Arimo:wght@400;700&display=swap" rel="stylesheet">
<style>
:root{
  --page:#e6e6e6;
  --green:#8cc63f;
  --green-light:#a8d84e;
  --green-dark:#6aa524;
  --green-text:#4f8f2a;
  --grey-text:#5a5a5a;
  --body-text:#8a8a8a;
  --menu-text:#2e2e2e;
  --panel-top:#ffffff;
  --panel-bottom:#dcdcdc;
  --hero-dark:#0b1216;
  --hero-mid:#1e3346;
  --hero-blue:#5d7f9f;
  --footer:#2b2b2b;
  --white:#ffffff;
  --tile:#f2f2f2;
  --tile-inner:#3a3a3a;
}
*{margin:0;padding:0;box-sizing:border-box}
html,body{width:1200px;height:953px;overflow:hidden}
body{background:var(--page);position:relative;font-family:"PT Sans",sans-serif}
.side-panel{position:absolute;left:35px;top:0;width:278px;height:378px;background:linear-gradient(to bottom,var(--panel-top),var(--panel-bottom))}
.brand{position:absolute;left:22px;top:48px;display:flex;align-items:center;gap:10px}
.brand-mark{width:26px;height:26px;background:var(--green)}
.brand-name{font-family:"PT Sans Narrow",sans-serif;font-weight:700;font-size:34px;color:var(--grey-text);letter-spacing:.5px;line-height:1}
.tagline{position:absolute;left:55px;top:114px;font-style:italic;font-size:16px;color:var(--grey-text)}
.main-menu{position:absolute;left:24px;top:168px;list-style:none}
.main-menu li{font-family:"PT Sans Narrow",sans-serif;font-size:22px;color:var(--menu-text);line-height:28.4px}
.connect{position:absolute;left:36px;top:334px;font-style:italic;font-size:28px;color:var(--grey-text)}
.contact-bar{position:absolute;left:313px;top:0;width:852px;height:69px;background:linear-gradient(to bottom,var(--green-light),var(--green-dark))}
.contact-item{position:absolute;top:19px;display:flex;align-items:center;gap:18px;color:var(--white);font-weight:700;font-size:15px}
.contact-icon{width:38px;height:38px;border-radius:50%;background:radial-gradient(circle at 40% 35%,#fff,#c9c9c9);display:flex;align-items:center;justify-content:center;color:#555;font-size:22px;font-weight:700}
.hero{position:absolute;left:313px;top:70px;width:852px;height:308px;
  background:
    radial-gradient(ellipse 260px 200px at 22% 30%,rgba(150,175,200,.55),rgba(150,175,200,0) 100%),
    radial-gradient(ellipse 360px 300px at 28% 60%,var(--hero-blue),var(--hero-mid) 55%,rgba(30,51,70,0) 100%),
    linear-gradient(to right,#2a4258 0%,#16232e 45%,var(--hero-dark) 70%,var(--hero-dark) 100%)}
.steps{position:absolute;right:18px;top:26px;display:flex;gap:16px;font-size:17px;color:#9a9a9a}
.steps span{display:flex;align-items:center;gap:8px}
.steps span::before{content:"";width:17px;height:17px;border-radius:50%;background:#6c6c6c}
.steps .active{color:var(--green)}
.steps .active::before{background:var(--green)}
.newsletter-band{position:absolute;left:35px;top:378px;width:1130px;height:51px;background:linear-gradient(to bottom,var(--green-light),var(--green-dark))}
.social{position:absolute;top:7px;width:38px;height:38px;border-radius:5px;background:linear-gradient(to bottom,#ffffff,#d8d8d8);box-shadow:0 1px 2px rgba(0,0,0,.35);display:flex;align-items:center;justify-content:center}
.social::after{content:"";width:26px;height:26px;border-radius:3px;background:var(--tile-inner)}
.newsletter-text{position:absolute;left:352px;top:11px;font-family:"Arimo",sans-serif;font-size:22px;color:var(--white);letter-spacing:-.3px}
.band-button{position:absolute;top:5px;height:41px;background:linear-gradient(to bottom,#fff,#e2e2e2);border-left:4px solid #bbb;font-family:"Arimo",sans-serif;font-size:16px;color:#111;display:flex;align-items:center;justify-content:center;text-align:center;line-height:1}
.welcome{position:absolute;left:235px;top:433px;width:730px;height:365px;background:#f4f4f4;border:1px solid #d4d4d4}
.welcome h1{position:absolute;left:165px;top:34px;font-family:"PT Sans",sans-serif;font-weight:400;font-size:29px;letter-spacing:-.5px;color:var(--grey-text)}
.welcome h1 .accent{color:var(--green-text)}
.welcome p{position:absolute;left:48px;width:660px;font-family:"Arimo",sans-serif;font-weight:700;font-size:13px;line-height:21px;color:var(--body-text);letter-spacing:-.45px}
.footer{position:absolute;left:0;top:809px;width:1200px;height:144px;background:var(--footer);font-family:"Arimo",sans-serif;color:var(--white)}
.footer-links{position:absolute;top:35px;left:0;width:100%;font-size:14px}
.footer-links span{position:absolute}
.footer-contact{position:absolute;left:242px;top:92px;font-size:15px}
.copyright{position:absolute;left:778px;top:93px;font-size:14px;color:#8a8a8a}
</style>
</head>
<body>
<aside class="side-panel">
  <div class="brand"><span class="brand-mark"></span><span class="brand-name">TESSARO LANE</span></div>
  <div class="tagline">Because You´re Awesome!</div>
  <ul class="main-menu">
    <li>STRATEGY</li><li>PORTFOLIO</li><li>ABOUT US</li><li>CONTACT US</li><li>BLOG</li>
  </ul>
  <div class="connect">Connect with us!</div>
</aside>

<header class="contact-bar">
  <div class="contact-item" style="left:319px"><span class="contact-icon">@</span>Email: info@tessarolane.ca</div>
  <div class="contact-item" style="left:609px"><span class="contact-icon"><svg width="20" height="20" viewBox="0 0 24 24"><path d="M6.6 2.5 9.3 6c.5.6.4 1.4-.1 2L7.8 9.4a13 13 0 0 0 6.8 6.8l1.4-1.4c.6-.5 1.4-.6 2-.1l3.5 2.7c.6.5.7 1.4.1 2l-1.7 1.8c-.8.8-2 1.1-3 .7A20 20 0 0 1 1.9 6.9c-.4-1 0-2.2.7-3l1.9-1.6c.6-.5 1.5-.4 2.1.2Z" fill="#555"/></svg></span>Phone: 555-013-4829</div>
</header>

<section class="hero" role="img" aria-label="Branding concept photograph: the words brand, essence, attribute and identity sketched with arrows on glass against a dark blue backdrop">
  <nav class="steps">
    <span class="active">Tessaro Lane</span><span>Be Found</span><span>Connect</span><span>Get Growing</span>
  </nav>
</section>

<div class="newsletter-band">
  <span class="social" style="left:58px" role="img" aria-label="Social network link"></span>
  <span class="social" style="left:117px" role="img" aria-label="Social network link"></span>
  <span class="social" style="left:173px" role="img" aria-label="Social network link"></span>
  <div class="newsletter-text">Get Tips and Tricks! Subscribe to our Newsletter.</div>
  <div class="band-button" style="left:871px;width:82px">Subscribe</div>
  <div class="band-button" style="left:1000px;width:116px">Get a Free<br>Quote!</div>
</div>

<main class="welcome">
  <h1><span class="accent">WELCOME TO</span> TESSARO LANE</h1>
  <p style="top:94px">This is just a bunch of words put toghether to make it look like&nbsp; paragraph. It is purly for show and filler so that we can have a general idea of what it will ook like when we put in the proper pagaraphs thatmake up our mission statment. I think this font size looks pretty good but maybe be a tad bit smaler.&nbsp; would like to see the welcome a little more dramatic looking. I think that</p>
  <p style="top:200px">is all I need to write here for now. This is just a bunch of words put toghether to make it look like&nbsp; paragraph. It is purly for show and filler so that we can have a general idea of what it will ook like when we put in the proper pagaraphs thatmake up our mission statment. I think this font size looks pretty good but maybe be a tad bit smaler.&nbsp; would like to see the welcome a little more dramatic looking. I think</p>
</main>

<footer class="footer">
  <div class="footer-links">
    <span style="left:244px">Site Map</span><span style="left:323px">/</span>
    <span style="left:365px">Strategy</span><span style="left:452px">/</span>
    <span style="left:498px">Portfolio</span><span style="left:592px">/</span>
    <span style="left:645px">About Us</span><span style="left:742px">/</span>
    <span style="left:790px">Contact Us</span><span style="left:897px">/</span>
    <span style="left:939px">Blog</span>
  </div>
  <div class="footer-contact">Contact info &nbsp;: Email: info@tessarolane.ca &nbsp;&nbsp;&nbsp;&nbsp;Phone: 555-013-4829</div>
  <div class="copyright">©TESSARO LANE INC. 2013</div>
</footer>
</body>
</html>
```